Life Coach for Lawyers Business Card Design

Elegant, original, business card design for life coaching service for associate attorneys who work in big law and struggle with stress, overwhelm, and time management. Double sided design.

Target Market(s)

Women associate attorneys who work in big law and struggle with stress, overwhelm, and time management.

Industry/Entity Type

Life Coaching

Contact Information for Business Card

Marissa Pendrell
Life Coach
518.677.3941
calmbriefcounsel.net
marissa@calmbriefcounsel.net
@calmbriefcounsel (Instagram)

Font styles to use
Other font styles liked:
• Silver South font duo. See uploaded files.

Requirements
Must have
• Icons for phone, website, email, and Instagram instead of words. Specific colors used in my logo (171B2B, 421121, FFFFFF)
Nice to have
• Foil. Embossed. Feminine design.
Should not have
• Any colors other than those used in logo. See uploaded files.

```html
<!DOCTYPE html>
<html lang="en">
<head>
<meta charset="utf-8">
<title>Calm Brief Counsel – Business Card</title>
<link rel="stylesheet" href="https://fonts.googleapis.com/css2?family=Playfair+Display:wght@500;700&family=Questrial&display=swap">
<style>
  :root {
    --page: #2b2b2e;
    --paper: #ffffff;
    --wine: #421121;
    --navy: #171b2b;
    --plum: #4a3550;
    --ink-grey: #6b6b70;
    --white: #ffffff;
  }
  * { box-sizing: border-box; margin: 0; padding: 0; }
  html, body {
    width: 1200px; height: 900px; overflow: hidden;
    background: var(--page);
  }
  .stage {
    width: 1200px; height: 900px;
    display: flex; align-items: center; justify-content: center; gap: 44px;
  }
  .card {
    position: relative;
    width: 540px; height: 309px;
    border-radius: 4px;
    overflow: hidden;
    box-shadow: 0 10px 28px rgba(0,0,0,.45);
  }

  /* Front */
  .card-front { background: var(--paper); }
  .brand {
    position: absolute; left: 52px; top: 58px;
    font-family: "Playfair Display", serif; font-weight: 500;
    color: var(--wine);
    font-size: 34px; line-height: 1.05; letter-spacing: .5px;
  }
  .contact-block {
    position: absolute; left: 250px; top: 150px;
    font-family: "Questrial", sans-serif; color: var(--ink-grey);
  }
  .person-name {
    font-family: "Playfair Display", serif; font-weight: 700;
    color: var(--wine); font-size: 19px; letter-spacing: 1px;
    text-transform: uppercase;
  }
  .person-role { font-size: 13px; margin: 2px 0 10px; }
  .contact-list { list-style: none; }
  .contact-list li {
    display: flex; align-items: center; gap: 9px;
    font-size: 13.5px; line-height: 20px;
  }
  .contact-list svg { width: 12px; height: 12px; flex: none; fill: var(--wine); }

  /* Back */
  .card-back {
    background: radial-gradient(ellipse at 30% 60%, var(--plum) 0%, #3a2238 45%, var(--wine) 75%, var(--navy) 120%);
  }
  .back-motif {
    position: absolute; left: 34px; top: 30px;
    font-family: "Playfair Display", serif; font-weight: 500;
    font-size: 50px; color: rgba(255,255,255,.08);
  }
  .back-brand {
    position: absolute; right: 40px; bottom: 40px;
    font-family: "Playfair Display", serif; font-weight: 500;
    color: var(--white); font-size: 28px; line-height: 1.05; text-align: right;
  }
</style>
</head>
<body>
<main class="stage">
  <section class="card card-front" aria-label="Card front">
    <div class="brand">Calm Brief<br>Counsel</div>
    <div class="contact-block">
      <h1 class="person-name">Marissa Pendrell</h1>
      <p class="person-role">Life Coach</p>
      <ul class="contact-list">
        <li><svg viewBox="0 0 24 24" aria-hidden="true"><path d="M6.6 10.8c1.4 2.8 3.8 5.1 6.6 6.6l2.2-2.2c.3-.3.7-.4 1-.2 1.1.4 2.3.6 3.6.6.6 0 1 .4 1 1V20c0 .6-.4 1-1 1C10.6 21 3 13.4 3 4c0-.6.4-1 1-1h3.5c.6 0 1 .4 1 1 0 1.3.2 2.5.6 3.6.1.3 0 .7-.2 1z"/></svg>518.677.3941</li>
        <li><svg viewBox="0 0 24 24" aria-hidden="true"><path d="M2 21l21-9L2 3v7l15 2-15 2z"/></svg>marissa@calmbriefcounsel.net</li>
        <li><svg viewBox="0 0 24 24" aria-hidden="true"><circle cx="12" cy="12" r="10"/></svg>calmbriefcounsel.net</li>
        <li><svg viewBox="0 0 24 24" aria-hidden="true"><rect x="3" y="3" width="18" height="18" rx="3"/></svg>@calmbriefcounsel</li>
      </ul>
    </div>
  </section>

  <section class="card card-back" aria-label="Card back">
    <div class="back-motif">Calm Brief</div>
    <div class="back-brand">Calm Brief<br>Counsel</div>
  </section>
</main>
</body>
</html>
```